Kestrel FM
Stationary and Business card Design
Simple
Adaeze T. Ibekwe
Managing Director
14 Umuola Lane, Ekwe Ridge, Aba. Nigeria, West Africa.
atibekwe@kestrelfmx.com
www.kestrelfmx.com
There are place holders, so keep each layer separated, and put each item (e.g. telephone number, name,etc) on separate levels to allow easy editing in both ai and psd files.
Infinity logo sign

```html
<!DOCTYPE html>
<html lang="en">
<head>
<meta charset="utf-8">
<title>Kestrel FM Business Card</title>
<link href="https://fonts.googleapis.com/css2?family=Open+Sans:wght@400;600;800&display=swap" rel="stylesheet">
<style>
  :root {
    --brand-red: #ea1c2a;
    --ink: #1d1d1f;
    --muted: #7a7a7a;
    --body-text: #444444;
    --paper: #ffffff;
    --backdrop: #ffffff;
  }
  * { margin: 0; padding: 0; box-sizing: border-box; }
  html, body {
    width: 1200px; height: 876px; overflow: hidden;
    background: var(--backdrop);
    font-family: "Open Sans", Arial, sans-serif;
  }
  .stage { position: relative; width: 1200px; height: 876px; }
  .card {
    position: absolute; top: 326px;
    width: 440px; height: 264px;
    overflow: hidden;
    box-shadow: 0 6px 14px rgba(0,0,0,0.18);
  }
  .card--front { left: 132px; background: var(--paper); }
  .card--back { left: 612px; background: var(--brand-red); }
  .card svg.shapes { position: absolute; inset: 0; }

  .wordmark {
    position: absolute;
    display: flex; align-items: center; gap: 5px;
    font-weight: 800; color: var(--ink);
    white-space: nowrap; letter-spacing: -0.5px;
    transform: translate(-50%, -50%);
  }
  .wordmark__dot { border-radius: 50%; background: var(--brand-red); flex: none; }
  .card--front .wordmark { left: 112px; top: 76px; font-size: 20px; }
  .card--front .wordmark__dot { width: 11px; height: 11px; }
  .card--back .wordmark { left: 220px; top: 132px; font-size: 30px; }
  .card--back .wordmark__dot { width: 16px; height: 16px; }

  .holder { position: absolute; left: 233px; top: 114px; }
  .holder__name { color: var(--brand-red); font-weight: 600; font-size: 20px; line-height: 1.1; }
  .holder__title { color: var(--muted); font-size: 14px; margin-top: 3px; }

  .contact { position: absolute; font-size: 11px; color: var(--body-text); line-height: 1.35; }
  .contact-row { display: flex; align-items: flex-start; gap: 7px; }
  .contact-row + .contact-row { margin-top: 6px; }
  .contact-icon { width: 13px; height: 13px; flex: none; margin-top: 1px; }
  .contact--left { left: 16px; top: 190px; }
  .contact--right { left: 256px; top: 190px; }
</style>
</head>
<body>
<main class="stage">
  <section class="card card--front" aria-label="Business card front">
    <svg class="shapes" width="440" height="264" viewBox="0 0 440 264">
      <rect x="0" y="0" width="440" height="88" fill="var(--brand-red)"/>
      <circle cx="112" cy="106" r="80" fill="var(--paper)"/>
    </svg>
    <div class="wordmark"><span>Kestrel</span><span class="wordmark__dot"></span><span>FM</span></div>
    <div class="holder">
      <p class="holder__name">Adaeze T. Ibekwe</p>
      <p class="holder__title">Managing Director</p>
    </div>
    <div class="contact contact--left">
      <div class="contact-row">
        <svg class="contact-icon" viewBox="0 0 14 14"><circle cx="7" cy="7" r="7" fill="var(--brand-red)"/><path d="M3.5 7.2 7 4.2l3.5 3V10h-2.3V8.2H5.8V10H3.5z" fill="#fff"/></svg>
        <span>14 Umuola Lane, Ekwe Ridge,<br>Aba. Nigeria, West Africa.</span>
      </div>
      <div class="contact-row">
        <svg class="contact-icon" viewBox="0 0 14 14"><circle cx="7" cy="7" r="7" fill="var(--brand-red)"/><circle cx="7" cy="7" r="3.6" fill="none" stroke="#fff" stroke-width="1"/><path d="M3.4 7h7.2M7 3.4c-1.6 2-1.6 5.2 0 7.2M7 3.4c1.6 2 1.6 5.2 0 7.2" fill="none" stroke="#fff" stroke-width="0.8"/></svg>
        <span>www.kestrelfmx.com</span>
      </div>
    </div>
    <div class="contact contact--right">
      <div class="contact-row">
        <svg class="contact-icon" viewBox="0 0 14 14"><circle cx="7" cy="7" r="7" fill="var(--brand-red)"/><rect x="3.6" y="4.6" width="6.8" height="4.8" fill="none" stroke="#fff" stroke-width="0.9"/><path d="M3.6 4.8 7 7.4l3.4-2.6" fill="none" stroke="#fff" stroke-width="0.9"/></svg>
        <span>atibekwe@kestrelfmx.com</span>
      </div>
      <div class="contact-row">
        <svg class="contact-icon" viewBox="0 0 14 14"><circle cx="7" cy="7" r="7" fill="var(--brand-red)"/><path d="M4.6 3.8c.5-.3 1 0 1.3.6l.4.9c.1.4 0 .7-.3.9l-.4.3c.4.9 1.1 1.6 2 2l.3-.4c.2-.3.5-.4.9-.3l.9.4c.6.3.9.8.6 1.3-.4.7-1.1 1-1.9.8C6.3 9.7 4.3 7.7 3.8 5.6c-.2-.8.1-1.4.8-1.8z" fill="#fff"/></svg>
        <span>+555-555-5555<br>+555-555-5555</span>
      </div>
    </div>
  </section>

  <section class="card card--back" aria-label="Business card back">
    <svg class="shapes" width="440" height="264" viewBox="0 0 440 264">
      <rect x="0" y="92" width="440" height="88" fill="var(--paper)"/>
      <circle cx="220" cy="132" r="112" fill="var(--paper)"/>
    </svg>
    <div class="wordmark"><span>Kestrel</span><span class="wordmark__dot"></span><span>FM</span></div>
  </section>
</main>
</body>
</html>
```